Harbor Dental, LLC business card project

Business card to be designed with current logo.
Dental office- please keep design of card that looks clean and professional.
Please include the following info:
Harbor Dental, LLC
Dr. Corinne Pelham
3187 Elmwood
Bethlehem, PA 18015
610-392-7158
harbordental.office@quillmail.net
Updates
Hello everyone-
Project Deadline Extended
Reason: Just got back from overseas- will look at all designs and provide feedback. Thank you!
Project Deadline Extended
Reason: Polling my friends for the final selection-
thank you to all those that participated- so many talented designers!
Business

```html
<!DOCTYPE html>
<html lang="en">
<head>
<meta charset="utf-8">
<title>Harbor Dental — Business Card Options</title>
<link rel="stylesheet" href="https://fonts.googleapis.com/css2?family=PT+Sans:wght@400;700&family=Cinzel:wght@600&display=swap">
<style>
  :root {
    --backdrop: #6e4328;
    --card-white: #ffffff;
    --leaf-green: #67a143;
    --lime: #b2d235;
    --ink: #333333;
    --label: #f4ece4;
    --shadow: rgba(0, 0, 0, 0.35);
  }
  * { margin: 0; padding: 0; box-sizing: border-box; }
  html, body { width: 1200px; height: 775px; overflow: hidden; }
  body {
    position: relative;
    background: var(--backdrop);
    font-family: "PT Sans", Arial, sans-serif;
  }
  .card {
    position: absolute;
    width: 510px;
    height: 290px;
    border-radius: 22px;
    overflow: hidden;
    box-shadow: 3px 5px 10px var(--shadow);
  }
  .card--front { left: 83px; top: 80px; background: var(--card-white); }
  .card--back-white { left: 620px; top: 77px; background: var(--card-white); }
  .card--back-lime { left: 77px; top: 405px; background: var(--lime); }
  .card--back-green { left: 620px; top: 405px; background: var(--leaf-green); }

  .option-label {
    position: absolute;
    color: var(--label);
    font-size: 21px;
  }
  .option-label--1 { left: 1029px; top: 41px; }
  .option-label--2 { left: 90px; top: 709px; }
  .option-label--3 { left: 1022px; top: 711px; }

  .brand {
    position: absolute;
    display: flex;
    align-items: center;
    gap: 12px;
    white-space: nowrap;
    font-weight: 400;
  }
  .brand__dot {
    width: 22px; height: 22px;
    border-radius: 50%;
  }
  .card--front .brand { left: 16px; top: 68px; font-size: 42px; color: var(--leaf-green); }
  .card--front .brand__dot { background: var(--lime); }
  .brand--centered { left: 50%; top: 50%; transform: translate(-50%, -50%); }
  .card--back-white .brand { font-size: 40px; color: var(--leaf-green); }
  .card--back-white .brand__dot { background: var(--lime); }
  .card--back-lime .brand,
  .card--back-green .brand { font-size: 34px; color: var(--card-white); }
  .card--back-lime .brand__dot,
  .card--back-green .brand__dot { background: var(--card-white); }

  .phone {
    position: absolute;
    right: 34px; top: 26px;
    font-size: 14px;
    color: var(--ink);
  }
  .address {
    position: absolute;
    left: 30px; top: 152px;
    font-size: 13px;
    line-height: 21px;
    color: var(--ink);
    font-style: normal;
  }
  .address strong { font-weight: 700; }
  .address .email { letter-spacing: 0.6px; }

  .wave { position: absolute; left: 0; bottom: 0; width: 510px; height: 90px; }
  .doctor {
    position: absolute;
    left: 30px; bottom: 20px;
    font-family: "Cinzel", Georgia, serif;
    font-weight: 600;
    font-size: 19px;
    letter-spacing: 0.5px;
    color: var(--card-white);
  }
</style>
</head>
<body>
  <p class="option-label option-label--1">option 1</p>
  <p class="option-label option-label--2">option 2</p>
  <p class="option-label option-label--3">option 3</p>

  <section class="card card--front">
    <p class="phone">Tel: 610-392-7158</p>
    <div class="brand"><span class="brand__dot"></span>Harbor Dental</div>
    <address class="address">
      3187 Elmwood, Bethlehem, PA 18015<br>
      <strong>email:</strong> <span class="email">harbordental.office@quillmail.net</span>
    </address>
    <svg class="wave" viewBox="0 0 510 90" aria-hidden="true">
      <path d="M0 22 C120 -6 250 10 340 30 C420 46 470 34 510 20 L510 90 L0 90 Z" fill="var(--leaf-green)"/>
      <path d="M110 0 C230 8 320 40 400 42 C450 42 485 28 510 14 L510 4 C480 20 450 34 400 34 C320 32 240 6 110 0 Z" fill="var(--lime)"/>
      <path d="M0 22 C120 -6 250 10 340 30 C420 46 470 34 510 20" fill="none" stroke="var(--card-white)" stroke-width="3"/>
    </svg>
    <p class="doctor">Dr. Corinne Pelham</p>
  </section>

  <section class="card card--back-white">
    <div class="brand brand--centered"><span class="brand__dot"></span>Harbor Dental</div>
  </section>

  <section class="card card--back-lime">
    <div class="brand brand--centered"><span class="brand__dot"></span>Harbor Dental</div>
  </section>

  <section class="card card--back-green">
    <div class="brand brand--centered"><span class="brand__dot"></span>Harbor Dental</div>
  </section>
</body>
</html>
```